Walk Beside The River

Business Card design

Target Market(s)

People who require support in the commnity

Industry/Entity Type

Mental Health Support

Contact Information for Business Card

Mental Health Support Rosalind Tavener walkbesidetheriver@mailbrook.com.au 0458 906 312 PO Box 627 Coralwood QLD 4573

Colors
6B429C
8869AF
B7A5CE
E3DAEB
F3F0F8

Requirements
Must have
• Logo & details listed above
Should not have
• No red or orange

```html
<!DOCTYPE html>
<html lang="en">
<head>
<meta charset="utf-8">
<title>Walk Beside The River – Business Card</title>
<link href="https://fonts.googleapis.com/css2?family=Inter:wght@400;600&display=swap" rel="stylesheet">
<style>
  :root {
    --purple: #6B429C;
    --purple-mid: #8869AF;
    --paper: #F1F0ED;
    --backdrop: #DCDDDF;
    --ink-grey: #6E6E70;
  }
  html, body {
    margin: 0;
    padding: 0;
    width: 1200px;
    height: 1051px;
    overflow: hidden;
    background: var(--backdrop);
    font-family: "Inter", Arial, sans-serif;
  }
  .canvas {
    position: relative;
    width: 1200px;
    height: 1051px;
  }
  .card {
    position: absolute;
    left: 220px;
    width: 760px;
    height: 434px;
    background: var(--paper);
    border-bottom: 8px solid var(--purple);
    box-shadow: 0 18px 40px rgba(0,0,0,0.18);
    box-sizing: border-box;
  }
  .card--front { top: 68px; }
  .card--back  { top: 555px; border-bottom-width: 12px; }

  /* Front */
  .details {
    position: absolute;
    top: 120px;
    left: 0;
    right: 0;
    display: flex;
    justify-content: center;
    align-items: flex-start;
    gap: 20px;
  }
  .identity {
    text-align: right;
    color: var(--purple);
    font-weight: 600;
    font-size: 27px;
    line-height: 1.22;
  }
  .contact-group {
    display: flex;
    align-items: stretch;
    gap: 20px;
    margin-top: 50px;
  }
  .divider {
    width: 2px;
    background: var(--purple);
  }
  .contact {
    color: var(--ink-grey);
    font-size: 19px;
    line-height: 1.4;
    font-weight: 400;
    padding: 4px 0;
  }
  .contact-line {
    display: flex;
    align-items: center;
    gap: 8px;
  }
  .contact-icon {
    width: 16px;
    height: 16px;
    flex: none;
    fill: var(--purple);
  }

  /* Back */
  .brand {
    position: absolute;
    inset: 0;
    display: flex;
    flex-direction: column;
    align-items: center;
    justify-content: center;
    gap: 20px;
  }
  .brand-dot {
    width: 130px;
    height: 130px;
    border-radius: 50%;
    background: var(--purple);
  }
  .brand-name {
    color: var(--purple);
    font-weight: 600;
    font-size: 24px;
    letter-spacing: 0.04em;
  }
</style>
</head>
<body>
<main class="canvas">
  <section class="card card--front" aria-label="Business card front">
    <div class="details">
      <div class="identity">
        <div class="service">Mental Health Support</div>
        <div class="person">Rosalind Tavener</div>
      </div>
      <div class="contact-group">
        <div class="divider"></div>
        <div class="contact">
          <div class="contact-line">PO Box 627</div>
          <div class="contact-line">Coralwood QLD 4573</div>
          <div class="contact-line">
            <svg class="contact-icon" viewBox="0 0 24 24" aria-hidden="true"><path d="M6.6 10.8a15.1 15.1 0 0 0 6.6 6.6l2.2-2.2c.3-.3.7-.4 1-.2 1.1.4 2.3.6 3.6.6.6 0 1 .4 1 1V20c0 .6-.4 1-1 1C10.6 21 3 13.4 3 4c0-.6.4-1 1-1h3.5c.6 0 1 .4 1 1 0 1.3.2 2.5.6 3.6.1.3 0 .7-.2 1l-2.3 2.2z"/></svg>
            <span>0458 906 312</span>
          </div>
          <div class="contact-line">
            <svg class="contact-icon" viewBox="0 0 24 24" aria-hidden="true"><path d="M2 5h20v14H2z M3 6l9 7 9-7" fill="none" stroke="#6B429C" stroke-width="2"/></svg>
            <span>walkbesidetheriver@mailbrook.com.au</span>
          </div>
        </div>
      </div>
    </div>
  </section>

  <section class="card card--back" aria-label="Business card back">
    <div class="brand">
      <div class="brand-dot"></div>
      <div class="brand-name">Walk Beside The River</div>
    </div>
  </section>
</main>
</body>
</html>
```